New business card for UK roofing company

We are Brindmore Roofing and we need a business card design for our staff.

We offer the following services:

- New roofs
- General roof repairs
- Drone surveys
- Single ply roofing
- Steel cladding
- Asbestos removal
- Electronic leak detection

I have attached our logo. I have also attached example branding printed to our vans. The business card should fit in with the style of our branding.

The business card should have the following information;

Address:
Unit 17c Wendlecroft Farm
Wendlecroft Lane
Hatchington
CM4 9QD

Telephone: 020 7946 0372
24 Hour: 0800 612 4479

Email: ray@brindmoreroofing.example
Mobile: 07700981234
Name: Ray Tunstead
Website: www.brindmoreroofing.example

The business card will be printed in Spot UV, see here: https://www.kestaprint.example/business-cards/spot-uv/

If you need anymore info, please let me know,

```html
<!DOCTYPE html>
<html lang="en">
<head>
<meta charset="utf-8">
<title>Brindmore Roofing – Business Card</title>
<link rel="stylesheet" href="https://fonts.googleapis.com/css2?family=Montserrat:wght@400;500;700;800&display=swap">
<style>
  :root {
    --navy: #0d4778;
    --navy-deep: #0a3a63;
    --cyan: #12acd9;
    --cyan-dark: #0a86ad;
    --paper: #f6f7f8;
    --ink: #1b4f82;
    --backdrop: #262626;
  }
  html, body {
    margin: 0;
    width: 1200px;
    height: 801px;
    overflow: hidden;
    background: var(--backdrop);
    font-family: "Montserrat", Arial, sans-serif;
  }
  .card {
    position: absolute;
    top: 246px;
    width: 540px;
    height: 309px;
    overflow: hidden;
    box-shadow: 0 10px 30px rgba(0,0,0,.45);
  }
  .card--front { left: 40px; background: var(--navy); }
  .card--back {
    left: 620px;
    background: linear-gradient(120deg, var(--navy) 0%, #1477ad 60%, var(--cyan) 100%);
  }
  .card__shapes { position: absolute; inset: 0; }

  /* front: identity side */
  .identity { position: absolute; left: 26px; top: 26px; width: 225px; color: var(--ink); }
  .brand { display: flex; align-items: center; gap: 7px; white-space: nowrap; }
  .brand__dot { width: 18px; height: 18px; border-radius: 50%; background: var(--cyan); flex: none; }
  .brand__name { font-weight: 700; font-size: 19px; color: var(--navy); letter-spacing: -0.3px; }
  .person {
    margin: 14px 0 10px;
    font-weight: 800;
    font-size: 19px;
    letter-spacing: 1px;
    text-transform: uppercase;
    white-space: nowrap;
  }
  .person__first { color: var(--navy); }
  .person__last { color: var(--cyan); }
  .address { font-size: 11.5px; line-height: 15px; color: #44566a; margin-bottom: 10px; white-space: nowrap; }
  .contacts { list-style: none; margin: 0; padding: 0; font-size: 11.5px; line-height: 16px; color: #44566a; white-space: nowrap; }
  .contacts li { display: flex; align-items: center; gap: 7px; }
  .contacts svg { width: 10px; height: 10px; fill: var(--cyan); flex: none; }

  /* front: services side */
  .services__title {
    position: absolute; left: 290px; top: 92px; height: 30px;
    line-height: 30px; font-weight: 700; font-size: 13px; color: #fff; white-space: nowrap;
  }
  .services__list {
    position: absolute; left: 306px; top: 136px;
    list-style: none; margin: 0; padding: 0;
    color: #fff; font-size: 12.5px; line-height: 20px; white-space: nowrap;
  }
  .services__list li::before {
    content: ""; display: inline-block; width: 5px; height: 5px;
    border-radius: 50%; background: var(--cyan); margin: 0 8px 2px 0;
  }

  /* back: spot UV wordmark */
  .back__mark {
    position: absolute; inset: 0;
    display: flex; align-items: center; justify-content: center; gap: 14px;
  }
  .back__dot { width: 56px; height: 56px; border-radius: 50%; background: rgba(10,58,99,.35); flex: none; }
  .back__name { font-weight: 700; font-size: 44px; color: rgba(10,58,99,.35); letter-spacing: -1px; white-space: nowrap; }
</style>
</head>
<body>

<section class="card card--front" aria-label="Business card front">
  <svg class="card__shapes" viewBox="0 0 540 309" aria-hidden="true">
    <polygon points="0,0 252,0 270,92 270,135 290,309 0,309" fill="var(--paper)"/>
    <polygon points="266,122 290,122 290,136" fill="var(--cyan-dark)"/>
    <polygon points="266,92 540,92 540,122 266,122 278,107" fill="var(--cyan)"/>
  </svg>

  <div class="identity">
    <div class="brand">
      <span class="brand__dot"></span>
      <span class="brand__name">Brindmore Roofing</span>
    </div>
    <div class="person"><span class="person__first">Ray</span> <span class="person__last">Tunstead</span></div>
    <div class="address">
      Unit 17c Wendlecroft Farm<br>
      Wendlecroft Lane Hatchington<br>
      CM4 9QD
    </div>
    <ul class="contacts">
      <li><svg viewBox="0 0 10 10"><rect x="2.5" y="0" width="5" height="10" rx="1"/></svg>07700981234</li>
      <li><svg viewBox="0 0 10 10"><path d="M2 0l2 2.5-1 1.5a6 6 0 0 0 3 3l1.5-1L10 8l-1.5 2C4 10 0 6 0 1.5z"/></svg>020 7946 0372</li>
      <li><svg viewBox="0 0 10 10"><circle cx="5" cy="5" r="5"/></svg>0800 612 4479</li>
      <li><svg viewBox="0 0 10 10"><path d="M0 2h10v6H0z"/></svg>ray@brindmoreroofing.example</li>
      <li><svg viewBox="0 0 10 10"><circle cx="5" cy="5" r="5"/></svg>www.brindmoreroofing.example</li>
    </ul>
  </div>

  <div class="services__title">We offer the following services:</div>
  <ul class="services__list">
    <li>New roofs</li>
    <li>General roof repairs</li>
    <li>Drone surveys</li>
    <li>Single ply roofing</li>
    <li>Steel cladding</li>
    <li>Asbestos removal</li>
    <li>Electronic leak detection</li>
  </ul>
</section>

<section class="card card--back" aria-label="Business card back">
  <div class="back__mark">
    <span class="back__dot"></span>
    <span class="back__name">Brindmore Roofing</span>
  </div>
</section>

</body>
</html>
```